Danish Private Senior Care provider Solvænge needs new Advertisement Design

Solvænge, one of the largest private Senior Care providers in Denmark, needs new design ideas for our printed advertisements.
The advertisement design will be used in newspapers, brochures and journals. We are looking for a graphic design that make our ads easily recognisable as Solvænge-ads and communicate Solvænge as a trustworthy, competent and reliable provider of Senior Care, both to the private market and the public sector.
As the texts we will use will vary the task is to design the basic graphic layout.
Feel free to use pictures and text-examples from our web-page, www.solvaenge-pleje.dk. You will also see the look and colourscheme we use.

Target Market(s)

Our target market is senior Citizens and their families, as well as decision makers in the public sector.

Requirements
Must have
• Our logo (w. pay-off).
• Pay-off Translated: We are people caring for people

```html
<!DOCTYPE html>
<html lang="da">
<head>
<meta charset="utf-8">
<title>Solvænge – annonce</title>
<link rel="stylesheet" href="https://fonts.googleapis.com/css2?family=Noto+Serif:ital,wght@0,400;0,700;1,400&display=swap">
<style>
  :root {
    --red: #d8202a;
    --red-dark: #b3161f;
    --white: #ffffff;
    --ink: #111111;
    --grey-text: #8a8a8a;
    --grey-band: #b9b9bb;
    --sky-light: #d9eef5;
    --sky: #9fd3e6;
  }
  * { margin: 0; padding: 0; box-sizing: border-box; }
  html, body { width: 848px; height: 1200px; overflow: hidden; background: var(--white); }
  .ad {
    position: relative;
    width: 848px;
    height: 1200px;
    overflow: hidden;
    font-family: "Noto Serif", Georgia, serif;
    background: var(--white);
  }
  .hero-photo {
    position: absolute;
    left: 0; top: 0;
    width: 848px; height: 830px;
    background: radial-gradient(ellipse at 40% 45%, #f3e1d4 0%, #e9cdbd 22%, transparent 48%),
                radial-gradient(ellipse at 72% 40%, #efd8cb 0%, #e2c2b3 20%, transparent 42%),
                linear-gradient(180deg, var(--sky) 0%, var(--sky-light) 55%, #e8eef3 100%);
  }
  .hero-edge {
    position: absolute;
    left: 0; top: 0;
    width: 848px; height: 1200px;
  }
  .headline-flag {
    position: absolute;
    left: 0; top: 23px;
    width: 362px; height: 174px;
  }
  .headline {
    position: absolute;
    left: 26px; top: 26px;
    color: var(--white);
    font-style: italic;
    font-size: 37px;
    line-height: 41px;
  }
  .brand-tab {
    position: absolute;
    left: 267px; top: 720px;
    width: 330px; height: 150px;
  }
  .brand-name {
    position: absolute;
    left: 267px; top: 790px;
    width: 330px;
    text-align: center;
    color: var(--white);
    font-weight: 700;
    font-size: 46px;
    line-height: 56px;
  }
  .payoff {
    position: absolute;
    left: 0; top: 890px;
    width: 848px;
    text-align: center;
    color: var(--ink);
    font-weight: 700;
    font-size: 29px;
  }
  .address {
    position: absolute;
    left: 26px; top: 988px;
    color: var(--grey-text);
    font-size: 26px;
  }
  .phone {
    position: absolute;
    left: 26px; top: 1032px;
    color: var(--red);
    font-style: italic;
    font-size: 31px;
  }
  .body-copy {
    position: absolute;
    left: 455px; top: 947px;
    width: 365px;
    color: var(--grey-text);
    font-size: 16.5px;
    line-height: 21.6px;
    text-align: justify;
  }
  .footer-band {
    position: absolute;
    left: 0; top: 1147px;
    width: 848px; height: 53px;
    background: var(--red);
    color: var(--white);
    text-align: center;
    font-style: italic;
    font-size: 36px;
    line-height: 53px;
  }
</style>
</head>
<body>
<main class="ad">
  <div class="hero-photo" role="img" aria-label="Photo of a smiling elderly couple, cheek to cheek, against a light blue sky"></div>

  <svg class="hero-edge" viewBox="0 0 848 1200" aria-hidden="true">
    <path d="M0 716 Q424 822 848 716 L848 1200 L0 1200 Z" fill="var(--grey-band)"/>
    <path d="M0 734 Q424 840 848 734 L848 1200 L0 1200 Z" fill="var(--white)"/>
  </svg>

  <svg class="headline-flag" viewBox="0 0 362 174" aria-hidden="true">
    <path d="M0 0 L334 0 L360 84 L334 174 L0 174 Z" fill="var(--red)"/>
  </svg>
  <h1 class="headline">We are experts at<br>making you enjoy<br>the best part<br>of your life</h1>

  <svg class="brand-tab" viewBox="0 0 330 150" aria-hidden="true">
    <defs>
      <linearGradient id="tabRed" x1="0" y1="0" x2="0" y2="1">
        <stop offset="0" stop-color="var(--red)"/>
        <stop offset="1" stop-color="var(--red-dark)"/>
      </linearGradient>
    </defs>
    <path d="M0 33 L165 0 L330 33 L330 140 Q330 150 320 150 L10 150 Q0 150 0 140 Z" fill="url(#tabRed)"/>
  </svg>
  <div class="brand-name">Solvænge</div>

  <p class="payoff">Vi er mennesker, der passer på mennesker</p>

  <p class="address">Solvej 4B, 9800 Hjørring.</p>
  <p class="phone">Ring til os på&nbsp; 70 41 58 36.</p>

  <p class="body-copy">Lorem ipsum dolor sit amet, consectetur adipiscing elit. Pellentesque ultrices ac neque vitae pellentesque. Duis et cursus quam. Pellentesque cursus, quam ac ultricies tempor, ligula nisi imperdiet elit, vulputate molestie urna est a purus. Quisque sagittis elit felis, vitae dignissim ipsum vestibulum nec.</p>

  <footer class="footer-band">www.solvaenge-pleje.dk</footer>
</main>
</body>
</html>
```